Voltline Assemblies, Inc. Business Card

Voltline has three operating entities and I'm looking for a standard business card template that can be used for Voltline and the three operating entities that the logo just get swapped out, but has a very similar look and feel. Ultimately if someone had a business card from each, they assume the organizations are related because they all have the same look and feel.
Below are our websites and I will attached the logos for each entity:
https://www.voltlineassemblies.example/
https://www.brantoceramic.example/
https://www.omra-kfsd.example/
https://www.summitbreaker.example/

Target Market(s)

US Voltline

Industry/Entity Type

US Voltline

Contact Information for Business Card

Normal stuff

```html
<!DOCTYPE html>
<html lang="en">
<head>
<meta charset="utf-8">
<title>Voltline Assemblies – Business Card Family</title>
<link rel="stylesheet" href="https://fonts.googleapis.com/css2?family=Roboto:wght@400;500;700&family=Roboto+Condensed:wght@700&display=swap">
<style>
  :root{
    --page-bg:#d3d3d3;
    --card-bg:#ffffff;
    --ink:#2b2b2b;
    --volt-main:#1f2d6b; --volt-alt:#d2232a;
    --branto-main:#1d3563; --branto-alt:#4f86c6;
    --omra-main:#1e1d6b; --omra-alt:#6d6d6d;
    --summit-main:#4e7690; --summit-alt:#333333;
  }
  *{box-sizing:border-box;margin:0;padding:0}
  html,body{width:966px;height:1200px;overflow:hidden}
  body{background:var(--page-bg);font-family:"Roboto",Arial,sans-serif;color:var(--ink);position:relative}

  .card{position:absolute;width:447px;height:255px;background:var(--card-bg);border-radius:9px;overflow:hidden}
  .col-front{left:25px}.col-back{left:499px}
  .row-1{top:40px}.row-2{top:333px}.row-3{top:620px}.row-4{top:906px}

  .volt{--main:var(--volt-main);--alt:var(--volt-alt);--icon:var(--volt-alt)}
  .branto{--main:var(--branto-main);--alt:var(--branto-alt);--icon:var(--branto-main)}
  .omra{--main:var(--omra-main);--alt:var(--omra-alt);--icon:var(--omra-main)}
  .summit{--main:var(--summit-main);--alt:var(--summit-alt);--icon:var(--summit-main)}

  /* brand lockup */
  .brand{position:absolute;display:flex;flex-direction:column;align-items:center;text-align:center;color:var(--main)}
  .brand-mark{border-radius:50%;background:var(--main)}
  .brand-mark.square{border-radius:4px}
  .brand-name{font-weight:700;line-height:1.1;color:var(--main)}
  .brand-name .line{display:block}
  .brand-tag{color:var(--main);font-weight:500}

  .card-front .brand{left:137px;top:127px;transform:translate(-50%,-50%);width:160px}
  .card-front .brand-mark{width:40px;height:40px;margin-bottom:6px}
  .card-front .brand-name{font-size:15px}
  .card-front .brand-name .small{font-size:7.5px;letter-spacing:2px}
  .card-front .brand-tag{font-size:6px;margin-top:3px}

  .card-back .brand{left:223px;top:128px;transform:translate(-50%,-50%);width:220px}
  .card-back .brand-mark{width:56px;height:56px;margin-bottom:8px}
  .card-back .brand-name{font-size:21px}
  .card-back .brand-name .small{font-size:10.5px;letter-spacing:3px}
  .card-back .brand-tag{font-size:8px;margin-top:4px}

  /* contact block */
  .contact{position:absolute;left:224px;top:127px;transform:translateY(-50%);border-left:1px solid var(--main);padding-left:13px;font-size:10.3px;line-height:14px}
  .person-name{font-family:"Roboto Condensed",Arial,sans-serif;font-weight:700;font-size:12.5px;color:var(--main);line-height:13px}
  .person-title{font-size:11px;line-height:13px}
  .branto .person-title{color:var(--alt)}
  .address{margin-top:6px}
  .channels{margin-top:5px;list-style:none}
  .channels li{display:flex;align-items:center;gap:2px}
  .channels svg{width:8px;height:8px;fill:var(--icon)}

  .band{position:absolute;left:0;bottom:0;width:447px;height:8px}
  .band .band-main{fill:var(--main)}.band .band-alt{fill:var(--alt)}

  .site{position:absolute;left:0;right:0;top:230px;text-align:center;font-size:10px;font-weight:500;color:var(--ink)}
  .site strong{color:var(--main);font-weight:700}
</style>
</head>
<body>

<!-- Voltline -->
<section class="card card-front col-front row-1 volt">
  <div class="brand"><span class="brand-mark"></span><span class="brand-name"><span class="line">VOLTLINE</span><span class="line small">ASSEMBLIES, INC.</span></span></div>
  <div class="contact">
    <p class="person-name">DANIEL CORWIN</p><p class="person-title">President</p>
    <p class="address">4410 Ridgeview Drive<br>Suite 210, Fairhaven, AL 35099</p>
    <ul class="channels">
      <li><svg viewBox="0 0 10 10"><path d="M2 0l2 2-1 1.5c.6 1.4 1.6 2.4 3 3L7.5 5.5l2 2L8 10C3.5 9.5.5 6.5 0 2z"/></svg>555 014 2290</li>
      <li><svg viewBox="0 0 10 10"><path d="M0 2h10v6H0zM0 2l5 3.5L10 2" stroke="#fff" stroke-width=".8"/></svg>info@voltlineassemblies.example</li>
      <li><svg viewBox="0 0 10 10"><circle cx="5" cy="5" r="4.6"/><path d="M.5 5h9M5 .5v9M2 2.5q3 1.5 6 0M2 7.5q3-1.5 6 0" stroke="#fff" stroke-width=".6" fill="none"/></svg>www.voltlineassemblies.example</li>
    </ul>
  </div>
  <svg class="band" viewBox="0 0 447 8" preserveAspectRatio="none"><polygon class="band-main" points="0,0 254,0 246,8 0,8"/><polygon class="band-alt" points="258,0 447,0 447,8 250,8"/></svg>
</section>
<section class="card card-back col-back row-1 volt">
  <div class="brand"><span class="brand-mark"></span><span class="brand-name"><span class="line">VOLTLINE</span><span class="line small">ASSEMBLIES, INC.</span></span></div>
  <p class="site">www.<strong>voltlineassemblies</strong>.example</p>
</section>

<!-- Branto -->
<section class="card card-front col-front row-2 branto">
  <div class="brand"><span class="brand-mark square"></span><span class="brand-name"><span class="line">BRANTO-KSN, LLC.</span></span><span class="brand-tag">A Voltline Assemblies, Inc. Company</span></div>
  <div class="contact">
    <p class="person-name">DANIEL CORWIN</p><p class="person-title">President</p>
    <p class="address">118 W. County RT 9, Ste 2,<br>PO Box 71, Linden Falls OH,<br>USA, 44999</p>
    <ul class="channels">
      <li><svg viewBox="0 0 10 10"><path d="M2 0l2 2-1 1.5c.6 1.4 1.6 2.4 3 3L7.5 5.5l2 2L8 10C3.5 9.5.5 6.5 0 2z"/></svg>1 (555) 018-4470</li>
      <li><svg viewBox="0 0 10 10"><path d="M0 2h10v6H0zM0 2l5 3.5L10 2" stroke="#fff" stroke-width=".8"/></svg>info@brantoceramic.example</li>
      <li><svg viewBox="0 0 10 10"><circle cx="5" cy="5" r="4.6"/><path d="M.5 5h9M5 .5v9M2 2.5q3 1.5 6 0M2 7.5q3-1.5 6 0" stroke="#fff" stroke-width=".6" fill="none"/></svg>www.brantoceramic.example</li>
    </ul>
  </div>
  <svg class="band" viewBox="0 0 447 8" preserveAspectRatio="none"><polygon class="band-main" points="0,0 254,0 246,8 0,8"/><polygon class="band-alt" points="258,0 447,0 447,8 250,8"/></svg>
</section>
<section class="card card-back col-back row-2 branto">
  <div class="brand"><span class="brand-mark square"></span><span class="brand-name"><span class="line">BRANTO-KSN, LLC.</span></span><span class="brand-tag">A Voltline Assemblies, Inc. Company</span></div>
  <p class="site">www.<strong>brantoceramic</strong>.example</p>
</section>

<!-- Omra -->
<section class="card card-front col-front row-3 omra">
  <div class="brand"><span class="brand-name"><span class="line">OMRA</span><span class="line small">KINETIC FIELD SENSOR</span><span class="line small">DEVICES CORP.</span></span><span class="brand-tag">A Voltline Assemblies, Inc. Company</span></div>
  <div class="contact">
    <p class="person-name">DANIEL CORWIN</p><p class="person-title">President</p>
    <p class="address">PO Box 342<br>Ashford, NC 28999</p>
    <ul class="channels">
      <li><svg viewBox="0 0 10 10"><path d="M2 0l2 2-1 1.5c.6 1.4 1.6 2.4 3 3L7.5 5.5l2 2L8 10C3.5 9.5.5 6.5 0 2z"/></svg>1 (555) 013-6621</li>
      <li><svg viewBox="0 0 10 10"><path d="M0 2h10v6H0zM0 2l5 3.5L10 2" stroke="#fff" stroke-width=".8"/></svg>info@omra-kfsd.example</li>
      <li><svg viewBox="0 0 10 10"><circle cx="5" cy="5" r="4.6"/><path d="M.5 5h9M5 .5v9M2 2.5q3 1.5 6 0M2 7.5q3-1.5 6 0" stroke="#fff" stroke-width=".6" fill="none"/></svg>www.omra-kfsd.example</li>
    </ul>
  </div>
  <svg class="band" viewBox="0 0 447 8" preserveAspectRatio="none"><polygon class="band-main" points="0,0 254,0 246,8 0,8"/><polygon class="band-alt" points="258,0 447,0 447,8 250,8"/></svg>
</section>
<section class="card card-back col-back row-3 omra">
  <div class="brand"><span class="brand-name"><span class="line">OMRA</span><span class="line small">KINETIC FIELD SENSOR</span><span class="line small">DEVICES CORP.</span></span><span class="brand-tag">A Voltline Assemblies, Inc. Company</span></div>
  <p class="site">www.<strong>omra-kfsd</strong>.example</p>
</section>

<!-- Summit -->
<section class="card card-front col-front row-4 summit">
  <div class="brand"><span class="brand-mark"></span><span class="brand-name"><span class="line">SUMMIT BREAKER</span></span><span class="brand-tag">A Voltline Assemblies Inc. Company</span></div>
  <div class="contact">
    <p class="person-name">DANIEL CORWIN</p><p class="person-title">President</p>
    <p class="address">2760 Cedar Lane SE Fairhaven,<br>AL 35099</p>
    <ul class="channels">
      <li><svg viewBox="0 0 10 10"><path d="M2 0l2 2-1 1.5c.6 1.4 1.6 2.4 3 3L7.5 5.5l2 2L8 10C3.5 9.5.5 6.5 0 2z"/></svg>1 (555) 018-4470</li>
      <li><svg viewBox="0 0 10 10"><path d="M0 2h10v6H0zM0 2l5 3.5L10 2" stroke="#fff" stroke-width=".8"/></svg>info@brantoceramic.example</li>
      <li><svg viewBox="0 0 10 10"><circle cx="5" cy="5" r="4.6"/><path d="M.5 5h9M5 .5v9M2 2.5q3 1.5 6 0M2 7.5q3-1.5 6 0" stroke="#fff" stroke-width=".6" fill="none"/></svg>www.brantoceramic.example</li>
    </ul>
  </div>
  <svg class="band" viewBox="0 0 447 8" preserveAspectRatio="none"><polygon class="band-main" points="0,0 254,0 246,8 0,8"/><polygon class="band-alt" points="258,0 447,0 447,8 250,8"/></svg>
</section>
<section class="card card-back col-back row-4 summit">
  <div class="brand"><span class="brand-mark"></span><span class="brand-name"><span class="line">SUMMIT BREAKER</span></span><span class="brand-tag">A Voltline Assemblies Inc. Company</span></div>
  <p class="site">www.<strong>summitbreaker</strong>.example</p>
</section>

</body>
</html>
```